UNDER ONE [BRIGHT] LANTERN, Shape your path

We are looking for a cover refresh of an existing bestselling book that is going into 3rd edition print this year.
The book is an inspirational as well as educational book that has become recognized as one of the most comprehensive, actionable, personal and financial planning resources available today for families, individuals and business owners alike.
Comprised of three true stories of loss, learning to live and love again and a 30 page checklist at the back of the book it contains tips and strategies for everyone to help them to get their personal and financial lives in order while they can.
The cover must have the following:
1. Appeal to a broad audience/both personal and corporate
2. Include Mira Tollenkamp Bestselling Author
3. Include introduction of a new Afterword
4. 3rd Edition
5. Colors to remain the same – red, black and white
6. The title must remain in caps and the word [BRIGHT] must have the brackets around it
We have also added a current copy of the second edition to help you. For your information our website is www.thetollenkampcircle.example
Reason: We have narrowed it down to our top 3 designs. We are submitting the covers to our community for them to pick the top cover. Good luck to everyone

```html
<!DOCTYPE html>
<html lang="en">
<head>
<meta charset="utf-8">
<title>Under One [Bright] Lantern – Book Cover</title>
<link href="https://fonts.googleapis.com/css2?family=Montserrat:wght@400;500;700;800;900&family=Mr+Dafoe&display=swap" rel="stylesheet">
<style>
  :root {
    --brand-red: #c4292d;
    --ink: #2a2a2a;
    --paper: #ffffff;
    --backdrop: #ececec;
    --rule: #bdbdbd;
    --steel-light: #f4f4f4;
    --steel-mid: #d6d6d8;
    --steel-dark: #a9abae;
  }
  * { margin: 0; padding: 0; box-sizing: border-box; }
  html, body {
    width: 1200px;
    height: 801px;
    overflow: hidden;
    background: var(--backdrop);
  }
  .cover {
    position: absolute;
    left: 376px;
    top: 66px;
    width: 448px;
    height: 670px;
    background: var(--brand-red);
  }
  .cover-page {
    position: absolute;
    left: 13px;
    top: 13px;
    right: 13px;
    bottom: 48px;
    background: var(--paper);
  }
  .afterword-line {
    position: absolute;
    left: 45px;
    right: 45px;
    top: 24px;
    padding-bottom: 4px;
    border-bottom: 1px solid var(--rule);
    font-family: 'Montserrat', sans-serif;
    font-weight: 500;
    font-size: 12.2px;
    letter-spacing: 2.7px;
    color: var(--ink);
    text-align: center;
    white-space: nowrap;
  }
  .title {
    position: absolute;
    left: 0;
    right: 0;
    top: 115px;
    text-align: center;
    font-family: 'Montserrat', sans-serif;
    color: var(--ink);
  }
  .title-small {
    display: block;
    font-weight: 400;
    font-size: 31px;
    line-height: 1;
    letter-spacing: 0.5px;
  }
  .title-key {
    display: block;
    font-weight: 800;
    font-size: 58px;
    line-height: 1;
    margin: 4px 0 6px;
    color: var(--brand-red);
    letter-spacing: -1px;
  }
  .title-key .bracket { font-weight: 500; }
  .tagline {
    position: absolute;
    left: 0;
    right: 0;
    top: 268px;
    text-align: center;
    font-family: 'Mr Dafoe', cursive;
    font-size: 36px;
    color: #3a3a3a;
  }
  .pen-art {
    position: absolute;
    left: 49px;
    top: 336px;
    width: 328px;
    height: 273px;
  }
  .edition {
    position: absolute;
    right: 8px;
    bottom: 12px;
    font-family: 'Montserrat', sans-serif;
    font-weight: 700;
    font-size: 12px;
    color: #111;
  }
  .edition sup { font-size: 6px; vertical-align: 5px; }
  .author-band {
    position: absolute;
    left: 0;
    right: 0;
    bottom: 0;
    height: 48px;
    display: flex;
    align-items: center;
    justify-content: center;
    font-family: 'Montserrat', sans-serif;
    font-weight: 800;
    font-size: 24px;
    letter-spacing: 1.6px;
    color: var(--paper);
  }
</style>
</head>
<body>
  <div class="cover">
    <div class="cover-page">
      <p class="afterword-line">INTRODUCTION OF A NEW AFTERWORD</p>
      <h1 class="title">
        <span class="title-small">UNDER ONE</span>
        <span class="title-key"><span class="bracket">[</span>BRIGHT<span class="bracket">]</span></span>
        <span class="title-small">LANTERN</span>
      </h1>
      <p class="tagline">Shape your path</p>
      <svg class="pen-art" viewBox="0 0 328 273" role="img" aria-label="Illustration of a silver fountain pen nib rising from the bottom edge, framed by light swirling flourishes">
        <defs>
          <linearGradient id="penTone" x1="0" y1="0" x2="0" y2="1">
            <stop offset="0" stop-color="var(--paper)"/>
            <stop offset="0.45" stop-color="var(--steel-light)"/>
            <stop offset="1" stop-color="var(--steel-mid)"/>
          </linearGradient>
        </defs>
        <rect width="328" height="273" fill="url(#penTone)"/>
      </svg>
      <p class="edition">3<sup>RD</sup> EDITION</p>
    </div>
    <div class="author-band">MIRA TOLLENKAMP</div>
  </div>
</body>
</html>
```